Website Design for Freeze-Dried Food Manufacturing Company (Pet Food & Agri-Food)

We are looking for a high-level web designer to create a clean, modern, premium website design for Tarquel, a freeze-dried food manufacturing company operating in both the pet food and agri-food space.
This is not a basic website build β we are looking for a designer who understands brand positioning, layout, and user flow, not just visuals.
π― Project Objective
Design a website that:
Clearly communicates our capabilities and value proposition
Feels premium, credible, and product-driven
Guides users through a simple, intuitive journey
Clean and Crips
A critical requirement is clearly separating:
π Pet Food
π Agri-Food
These must feel like two distinct pathways within the same brand experience.
We have attached detailed documents outlining structure, layout, and messaging. These should be followed closely.
π What Success Looks Like
A high-impact homepage with strong visual hierarchy
Clear entry points into Pet Food and Agri-Food
Clean, intentional layout (not cluttered or template-like)
Thoughtful spacing, typography, and flow
A design that feels considered and elevated, not generic
π¨ Design Direction
We are aiming for a:
Minimal, premium aesthetic
Warm, natural color palette (creams, browns, muted tones)
Ingredient and product-focused visuals
Avoid:
Overly corporate / industrial styles
Generic SaaS-style layouts
Busy or over-designed interfaces
End Goal
A website that immediately communicates:
Who we are
What we do
Why weβre different
In a way that feels premium, clear, and easy to navigate.
Link to current website: https://tarquelfoods.example/
https://tarquelhealth.example/wp-admin/

```html
<!DOCTYPE html>
<html lang="en">
<head>
<meta charset="utf-8">
<title>Tarquel — Ingredients with Purpose</title>
<link href="https://fonts.googleapis.com/css2?family=Cormorant+Garamond:wght@400;500;600&family=Inter:wght@400;500;600&display=swap" rel="stylesheet">
<style>
:root{
  --brown:#5a3a1e;
  --dark:#2e2119;
  --gold:#a8792f;
  --cream:#f4eee8;
  --cream2:#efe7df;
  --text:#3a2e27;
  --muted:#5d524b;
  --white:#fff;
}
*{box-sizing:border-box;margin:0;padding:0}
html,body{width:1200px;height:2524px;overflow:hidden}
body{font-family:"Inter",sans-serif;color:var(--text);background:var(--cream);position:relative}
.serif{font-family:"Cormorant Garamond",serif}
a{color:inherit;text-decoration:none}
.btn{display:inline-flex;align-items:center;gap:6px;font-size:12px;font-weight:600;padding:0 20px;height:33px;border-radius:2px}
.btn-solid{background:var(--brown);color:var(--white)}
.btn-line{border:2px solid var(--white);color:var(--white)}
.arrow-circ{width:11px;height:11px;border:1.5px solid currentColor;border-radius:50%;display:inline-block;position:relative}
.arrow-circ::after{content:"";position:absolute;left:2px;top:3px;width:3px;height:3px;border-top:1.5px solid currentColor;border-right:1.5px solid currentColor;transform:rotate(45deg)}

/* header */
.site-header{position:absolute;top:0;left:0;width:1200px;height:98px;background:var(--white);display:flex;align-items:center}
.brand{position:absolute;left:50px;top:30px;font-size:40px;color:#8b5733;font-weight:400;letter-spacing:1px}
.nav{position:absolute;left:242px;top:52px;display:flex;font-size:13.5px;font-weight:500;color:#3a3a3a}
.nav a{padding:0 17px;border-right:1px solid #555;line-height:12px}
.nav a:last-child{border:none}
.nav a.active{color:var(--brown);position:relative}
.nav a.active::after{content:"";position:absolute;left:0;right:0;top:26px;height:2px;background:var(--gold)}
.nav-cta{position:absolute;right:52px;top:45px}

/* hero */
.hero{position:absolute;top:98px;left:0;width:1200px;height:512px;background:linear-gradient(90deg,#f1ebe3,#f5efe9)}
.hero-img{position:absolute;right:0;top:0;width:700px;height:434px;background:radial-gradient(circle at 55% 45%,#9a6c43 0,#c9a98a 30%,#e6dacd 60%,#f1ebe3 100%)}
.hero h1{position:absolute;left:50px;top:75px;font-size:44px;line-height:46px;font-weight:500;color:#3a2e27}
.hero p{position:absolute;left:50px;top:234px;width:450px;font-size:14px;line-height:21px;color:var(--muted)}
.hero .btn{position:absolute;left:50px;top:316px}
.hero-points{position:absolute;left:58px;top:382px;display:flex;gap:70px;font-family:"Cormorant Garamond",serif;font-size:13px;color:var(--muted)}
.hero-points div{display:flex;gap:10px;align-items:flex-start;width:180px}
.hero-points svg{flex:none}

/* category cards */
.card{position:absolute;top:533px;width:550px;height:488px;border-radius:22px;overflow:hidden;color:var(--white)}
.card-pet{left:44px;background:#2e2119}
.card-agri{left:610px;background:linear-gradient(135deg,#4b4434,#6c6348 55,#3d3a2d)}
.card .photo{position:absolute}
.card-pet .photo{right:30px;top:25px;width:250px;height:463px;border-radius:120px 120px 0 0;background:linear-gradient(180deg,#5a3d28,#c7a48a 45%,#7a4a2a)}
.card-agri .photo{left:0;top:0;width:550px;height:488px;background:radial-gradient(circle at 68% 40%,#b08a62 0,#7d6a4c 35%,rgba(60,56,44,.3) 70%)}
.card-inner{position:absolute;left:43px;top:45px}
.card-agri .card-inner{left:60px}
.badge{width:90px;height:90px;border:2px solid var(--white);border-radius:50%;display:flex;align-items:center;justify-content:center}
.card h2{font-family:"Cormorant Garamond",serif;font-weight:400;font-size:25px;margin-top:18px}
.card .lead{font-size:14px;line-height:20px;margin-top:14px;width:220px}
.card ul{list-style:none;margin-top:20px}
.card li{display:flex;align-items:center;gap:12px;font-size:14px;height:30px}
.card li svg{flex:none}
.card .btn{margin-top:20px;height:36px}

/* features strip */
.features{position:absolute;top:1100px;left:40px;width:1120px;height:190px;display:flex}
.feature{flex:1;text-align:center;border-right:1px solid #3a2e27;padding:14px 10px 0}
.feature:last-child{border:none}
.feature h3{font-family:"Cormorant Garamond",serif;font-weight:500;font-size:15px;color:var(--muted);margin-top:16px;line-height:18px}
.feature p{font-size:13px;line-height:19px;color:var(--muted);margin-top:14px}

/* purpose + trust */
.purpose{position:absolute;top:1335px;left:0;width:600px;height:462px;background:linear-gradient(180deg,#5a4632 0%,#4d4a35 55%,#3d5a2a 100%);color:var(--white)}
.purpose .eyebrow{position:absolute;left:42px;top:34px;font-size:14px;font-weight:600;color:#c6924a}
.purpose h2{position:absolute;left:42px;top:64px;font-size:44px;line-height:46px;font-weight:600;width:520px}
.purpose p{position:absolute;left:42px;top:178px;width:400px;font-size:13.5px;line-height:20px}
.purpose .btn{position:absolute;left:42px;top:245px;background:#5a3216}
.trust{position:absolute;top:1335px;left:600px;width:600px;height:462px;background:#f0e9e3}
.trust h2{position:absolute;left:42px;top:30px;font-size:46px;line-height:48px;font-weight:500;color:#3a2e27}
.trust-grid{position:absolute;left:42px;top:140px;width:514px;height:190px;background:#f4eee9;border-radius:12px;display:flex}
.trust-item{flex:1;text-align:center;border-right:1px solid #3a2e27;padding:14px 4px 0}
.trust-item:last-child{border:none}
.trust-item h3{font-family:"Cormorant Garamond",serif;font-weight:500;font-size:14px;color:var(--muted);margin-top:12px}
.trust-item p{font-size:12.5px;line-height:19px;color:var(--muted);margin-top:12px}
.partners{position:absolute;left:52px;top:350px;display:flex;gap:16px}
.partners span{display:block;width:114px;height:44px;border-radius:6px;background:#dcd2c8}
.dots{position:absolute;left:275px;top:414px;display:flex;gap:9px}
.dots i{width:4px;height:4px;border-radius:50%;background:#bbb}
.dots i.on{background:#222}

/* applications */
.apps{position:absolute;top:1797px;left:0;width:1200px;height:348px;background:#f3eee9;text-align:center}
.apps .eyebrow{position:absolute;left:0;right:0;top:49px;font-size:14px;font-weight:600;color:var(--gold)}
.apps h2{position:absolute;left:0;right:0;top:75px;font-size:46px;line-height:48px;font-weight:500;color:#3a2e27}
.apps p{position:absolute;left:310px;width:580px;top:195px;font-size:13.5px;line-height:21px;color:var(--muted)}
.apps .ctas{position:absolute;left:0;right:0;top:262px;display:flex;justify-content:center;gap:18px}
.apps .btn{height:36px;border-radius:20px}
.apps .btn-out{border:2px solid var(--brown);color:var(--brown)}
.deco{position:absolute;border-radius:50%}
.deco-l{left:150px;top:115px;width:140px;height:100px;background:radial-gradient(circle,#7a4a28 0,#d9c2a8 55%,transparent 72%)}
.deco-r{left:920px;top:110px;width:150px;height:110px;background:radial-gradient(circle,#c99a6a 0,#e6d6c2 55%,transparent 72%)}

/* footer */
.site-footer{position:absolute;top:2145px;left:0;width:1200px;height:379px;background:var(--dark);color:var(--white)}
.f-brand{position:absolute;left:52px;top:45px;font-size:28px;font-weight:400;letter-spacing:1px}
.f-about{position:absolute;left:53px;top:97px;width:225px;font-size:13.5px;line-height:20.5px}
.f-more{position:absolute;left:73px;top:240px;font-size:12px;color:#c49a4f}
.f-col{position:absolute;top:48px;font-size:13.5px;line-height:20.5px}
.f-col h4{font-weight:500;font-size:15.5px;color:#c49a4f;margin-bottom:13px}
.f-col ul{list-style:none}
.contact-line{display:flex;gap:8px}
.contact-line svg{flex:none;margin-top:4px}
.socials{display:flex;gap:8px;margin-top:14px}
.socials span{width:26px;height:26px;border-radius:50%;background:var(--white)}
.news-label{margin-top:30px;font-size:13.5px}
.news-input{margin-top:8px;width:202px;height:33px;background:var(--white);border-radius:2px;color:#999;font-size:12px;padding:9px 12px}
.news-btn{margin-top:9px;width:202px;height:33px;background:#a8792f;color:var(--white);font-size:12px;font-weight:600;display:flex;align-items:center;justify-content:center}
.copyright{position:absolute;left:0;right:0;top:294px;text-align:center;font-size:13.5px}
</style>
</head>
<body>

<header class="site-header">
  <div class="brand">Tarquel</div>
  <nav class="nav">
    <a class="active" href="#">Home</a>
    <a href="#">About / Our Story</a>
    <a href="#">Applications</a>
    <a href="#">Capabilities</a>
    <a href="#">Quality &amp; Traceability</a>
    <a href="#">Why Tarquel</a>
  </nav>
  <a class="btn btn-solid nav-cta" href="#">Contact <span class="arrow-circ"></span></a>
</header>

<section class="hero">
  <div class="hero-img" role="img" aria-label="Bowls of brown kibble and ingredient powder with a wooden scoop and green leaves"></div>
  <h1 class="serif">Ingredients with<br>Purpose. Solutions that<br>Nourish.</h1>
  <p>Tarquel transforms high-quality by-products into human-grade ingredients for pet food and agri-food industries through our closed-loop system.</p>
  <a class="btn btn-solid" href="#">Discover Our Solutions <span class="arrow-circ"></span></a>
  <div class="hero-points">
    <div><svg width="32" height="32" viewBox="0 0 32 32" fill="none" stroke="#a8792f" stroke-width="1.5"><path d="M6 16a10 10 0 0 1 18-6M26 16a10 10 0 0 1-18 6"/><path d="M16 22V12M16 16c-3-1-4-3-4-5 3 0 4 2 4 5zM16 15c3-1 4-3 4-5-3 0-4 2-4 5z"/></svg>Closed-Loop System</div>
    <div><svg width="28" height="30" viewBox="0 0 28 30" fill="none" stroke="#a8792f" stroke-width="1.5"><path d="M14 3l10 4v8c0 6-4 10-10 12C8 25 4 21 4 15V7z"/><circle cx="14" cy="15" r="5"/><path d="M11.5 15l2 2 3-3.5"/></svg>Human-Grade Ingredient Focus</div>
  </div>
</section>

<article class="card card-pet">
  <div class="photo" role="img" aria-label="Beagle puppy sitting behind a bowl of kibble"></div>
  <div class="card-inner">
    <div class="badge"><svg width="40" height="36" viewBox="0 0 40 36" fill="#fff"><ellipse cx="20" cy="25" rx="9" ry="7"/><ellipse cx="8" cy="15" rx="4" ry="5"/><ellipse cx="32" cy="15" rx="4" ry="5"/><ellipse cx="14" cy="6" rx="4" ry="5"/><ellipse cx="26" cy="6" rx="4" ry="5"/></svg></div>
    <h2>Pet Food</h2>
    <p class="lead">Nutritious, functional ingredients for healthier, happier pets.</p>
    <ul>
      <li><svg width="28" height="22" viewBox="0 0 28 22" fill="none" stroke="#a8792f" stroke-width="1.4"><path d="M2 10h24c0 6-5 10-12 10S2 16 2 10z"/><circle cx="9" cy="7" r="2"/><circle cx="15" cy="5" r="2"/><circle cx="20" cy="7" r="2"/></svg>Meals</li>
      <li><svg width="28" height="26" viewBox="0 0 28 26" fill="none" stroke="#a8792f" stroke-width="1.4"><circle cx="7" cy="6" r="3"/><circle cx="20" cy="6" r="3"/><circle cx="13" cy="13" r="3"/><circle cx="6" cy="20" r="3"/><circle cx="21" cy="20" r="3"/></svg>Toppers</li>
      <li><svg width="28" height="24" viewBox="0 0 28 24" fill="none" stroke="#a8792f" stroke-width="1.4"><path d="M6 20L22 4M4 18l4 4M20 2l4 4"/></svg>Treats</li>
      <li><svg width="28" height="28" viewBox="0 0 28 28" fill="none" stroke="#a8792f" stroke-width="1.4"><path d="M14 2l10 4v8c0 6-4 10-10 12C8 24 4 20 4 14V6z"/><path d="M10 14l3 3 5-6"/></svg>Functional Formats</li>
    </ul>
    <a class="btn btn-line" href="#">Explore Pet Food <span class="arrow-circ"></span></a>
  </div>
</article>

<article class="card card-agri">
  <div class="photo" role="img" aria-label="Bowl of ground plant powder with a wooden scoop and burlap sack"></div>
  <div class="card-inner">
    <div class="badge"><svg width="36" height="36" viewBox="0 0 36 36" fill="none" stroke="#fff" stroke-width="1.6"><path d="M14 32c0-10 4-16 16-20-2 10-8 14-16 14M14 32c0-6-2-10-8-12 0 6 3 9 8 10"/></svg></div>
    <h2>Agri-Food</h2>
    <p class="lead">High-quality ingredients and value-added formats that grow possibilities.</p>
    <ul style="margin-left:-16px">
      <li><svg width="28" height="26" viewBox="0 0 28 26" fill="none" stroke="#a8792f" stroke-width="1.4"><path d="M4 22C6 10 14 4 24 3c-1 10-8 17-20 19zM4 22l12-12"/></svg>Ingredients</li>
      <li><svg width="28" height="22" viewBox="0 0 28 22" fill="none" stroke="#a8792f" stroke-width="1.4"><path d="M2 18h24L18 8l-4 3-4-5z"/></svg>Powders</li>
      <li><svg width="28" height="28" viewBox="0 0 28 28" fill="none" stroke="#a8792f" stroke-width="1.4"><rect x="8" y="7" width="12" height="19" rx="2"/><path d="M10 2h8v5h-8zM14 13v8M10 17h8"/></svg>Value-Added Formats</li>
    </ul>
    <a class="btn btn-line" href="#" style="margin-left:-18px">Explore Agri-Food <span class="arrow-circ"></span></a>
  </div>
</article>

<section class="features">
  <div class="feature"><svg width="34" height="34" viewBox="0 0 32 32" fill="none" stroke="#a8792f" stroke-width="1.4"><path d="M6 16a10 10 0 0 1 18-6M26 16a10 10 0 0 1-18 6"/><path d="M16 22V12M16 16c-3-1-4-3-4-5 3 0 4 2 4 5zM16 15c3-1 4-3 4-5-3 0-4 2-4 5z"/></svg><h3>Closed-Loop System</h3><p>We reduce waste and create value through a circular approach.</p></div>
  <div class="feature"><svg width="30" height="32" viewBox="0 0 28 30" fill="none" stroke="#a8792f" stroke-width="1.4"><path d="M14 3l10 4v8c0 6-4 10-10 12C8 25 4 21 4 15V7z"/><circle cx="14" cy="15" r="5"/><path d="M11.5 15l2 2 3-3.5"/></svg><h3>Human-Grade Ingredient Focus</h3><p>Sourced responsibly. Processed carefully. Always held to human-grade standards.</p></div>
  <div class="feature"><svg width="30" height="34" viewBox="0 0 30 34" fill="none" stroke="#a8792f" stroke-width="1.4"><circle cx="15" cy="12" r="9"/><circle cx="15" cy="12" r="5"/><path d="M10 20l-2 12 7-4 7 4-2-12"/></svg><h3>Quality &amp; Traceability</h3><p>Every batch is tested, tracked, and held to the highest standards.</p></div>
  <div class="feature"><svg width="34" height="32" viewBox="0 0 34 32" fill="none" stroke="#a8792f" stroke-width="1.4"><path d="M3 30V16l8 5v-5l8 5v-5l8 5V4h4v26z"/><path d="M8 25h3M15 25h3M22 25h3"/></svg><h3>Scalable Production</h3><p>Consistent supply, advanced capabilities, ready to scale with your needs.</p></div>
  <div class="feature"><svg width="34" height="32" viewBox="0 0 34 32" fill="none" stroke="#a8792f" stroke-width="1.4"><path d="M3 30h28M6 30V18h8v12M18 30V14h10v16"/><path d="M23 14V8c0-3 2-5 5-5M23 8c-2 0-4-2-4-4"/></svg><h3>Separate Production Environments</h3><p>Dedicated facilities for pet food and agri-food ensure safety, integrity, and quality.</p></div>
  <div class="feature"><svg width="32" height="32" viewBox="0 0 32 32" fill="none" stroke="#a8792f" stroke-width="1.4"><circle cx="16" cy="16" r="12"/><path d="M4 16h24M16 4c-5 6-5 18 0 24M16 4c5 6 5 18 0 24"/></svg><h3>Sustainable Future</h3><p style="font-size:14px">Better ingredients. Better nutrition. Better future.</p></div>
</section>

<section class="purpose" role="img" aria-label="Hands holding soil with a small tree in front of green fields">
  <div class="eyebrow">Our Purpose</div>
  <h2 class="serif">We turn by-products into better outcomes.</h2>
  <p>By combining innovation, responsibility, and care, we create ingredients that nourish pets, people, and the planet.</p>
  <a class="btn btn-solid" href="#">Learn Our Story <span class="arrow-circ"></span></a>
</section>

<section class="trust">
  <h2 class="serif">Trusted by partners who<br>care</h2>
  <div class="trust-grid">
    <div class="trust-item"><svg width="34" height="30" viewBox="0 0 34 30" fill="none" stroke="#a8792f" stroke-width="1.4"><circle cx="17" cy="9" r="6"/><path d="M3 22c4 0 8-3 12-3h6M3 28c6 0 12-2 18-6l8-6"/></svg><h3>Responsible<br>Sourcing</h3><p>Ethically sourced ingredients with transparent supply chains.</p></div>
    <div class="trust-item" style="padding-top:22px"><svg width="30" height="32" viewBox="0 0 30 34" fill="none" stroke="#a8792f" stroke-width="1.4"><circle cx="15" cy="12" r="9"/><path d="M11 12l3 3 5-6M10 20l-2 12 7-4 7 4-2-12"/></svg><h3>Reliable Quality</h3><p>Strict quality control from sourcing to final production.</p></div>
    <div class="trust-item" style="padding-top:22px"><svg width="34" height="30" viewBox="0 0 34 30" fill="none" stroke="#a8792f" stroke-width="1.4"><path d="M2 10l7-4 8 5 8-5 7 4M5 12l9 9c2 2 4 2 6 0l9-9"/></svg><h3>Strong Partnerships</h3><p>Long-term collaboration focused on growth and consistency.</p></div>
    <div class="trust-item" style="padding-top:22px"><svg width="32" height="32" viewBox="0 0 32 32" fill="none" stroke="#a8792f" stroke-width="1.4"><circle cx="16" cy="16" r="5"/><path d="M16 3v6M16 23v6M3 16h6M23 16h6M7 7l4 4M21 21l4 4M25 7l-4 4M11 21l-4 4"/></svg><h3>Sustainable Impact</h3><p>Supporting a more circular and responsible food future.</p></div>
  </div>
  <div class="partners"><span></span><span></span><span></span><span></span></div>
  <div class="dots"><i></i><i class="on"></i><i></i><i></i></div>
</section>

<section class="apps">
  <div class="deco deco-l" role="img" aria-label="Bowl of kibble with jerky sticks"></div>
  <div class="deco deco-r" role="img" aria-label="Two small bowls of ingredient powders with a leaf"></div>
  <div class="eyebrow">Applications</div>
  <h2 class="serif">Solutions Designed for<br>Every Need</h2>
  <p>Explore our tailored applications and discover how Tarquel can help bring your products to life.</p>
  <div class="ctas">
    <a class="btn btn-solid" href="#">View Pet Food Applications &#10141;</a>
    <a class="btn btn-out" href="#">View Agri-Food Applications &#10141;</a>
  </div>
</section>

<footer class="site-footer">
  <div class="f-brand">Tarquel</div>
  <p class="f-about">Tarquel is a trusted partner in developing high-quality, human-grade ingredient solutions for pet food and agri-food industries worldwide.</p>
  <a class="f-more" href="#">Learn more about Tarquel &#10141;</a>
  <div class="f-col" style="left:338px">
    <h4>Quick Links</h4>
    <ul><li>Home</li><li>About</li><li>Applications</li><li>Capabilities</li><li>Quality &amp; Traceability</li><li>Why Tarquel</li></ul>
  </div>
  <div class="f-col" style="left:623px;width:260px">
    <h4>Contact</h4>
    <div class="contact-line"><svg width="12" height="12" viewBox="0 0 12 12" fill="#c49a4f"><path d="M2 1l3 0 1 3-2 1c1 2 2 3 3 3l1-2 3 1v3c-6 0-9-4-9-9z"/></svg>1.800.555.0142</div>
    <div class="contact-line"><svg width="12" height="10" viewBox="0 0 12 10" fill="#c49a4f"><path d="M0 0h12v10H0z"/><path d="M0 0l6 5 6-5" stroke="#2e2119" fill="none"/></svg>Sales: sales@tarquelfoods.example</div>
    <div class="contact-line"><svg width="12" height="10" viewBox="0 0 12 10" fill="#c49a4f" style="margin-top:14px"><path d="M0 0h12v10H0z"/><path d="M0 0l6 5 6-5" stroke="#2e2119" fill="none"/></svg>Accounts Payable:<br>ap@tarquelfoods.example</div>
    <div class="socials"><span></span><span></span><span></span></div>
  </div>
  <div class="f-col" style="left:908px;width:220px">
    <h4>Newsletter</h4>
    <p>Stay updated on the latest innovations and insights.</p>
    <p class="news-label">Email</p>
    <div class="news-input">Email address</div>
    <div class="news-btn">Subscribe &#10141;</div>
  </div>
  <div class="copyright">© Copyright 2026 Tarquel. All Rights Reserved.</div>
</footer>

</body>
</html>
```